qm - website template
website of specialist in neurosurgery, and teacher at the University in Milan
qm - website template - Education
Creative Brief
Education
Benedetto L. Caramuzza, MD (specialist in neurosurgery and in the history of medicine), historian and anthropologist, teaches history of medicine and health in the Faculty of Medicine, University of Velmora Castrene, where he directs the Institute for anatomical inquiry into past doctrines "(www.dulrota.it).
He's the author of over 250 papers in national and international partner to the history of medical and health disciplines and pharmacological institute of the Italian Ombrilla.
Traditional
blu (see attached logo file)
red (see attached logo file)
We need the graphic template of: • Homepage • Generic content page (text+image+ eventual document to download) • listing page of books + page with information about the selected book • listing page of conference + page with information about the selected conference • Contact The site must be optimized for 1024X768. For the main menu, it's possibile to use not system font. File must be preferably png (adobe fireworks), otherwise ai (adobe illustrator) or psd (adobe photoshop).

```html
<!DOCTYPE html>
<html lang="it">
<head>
<meta charset="utf-8">
<title>qm – Prof. Benedetto L. Caramuzza</title>
<link rel="stylesheet" href="https://fonts.googleapis.com/css2?family=Cuprum:wght@400;700&family=PT+Sans:wght@400;700&display=swap">
<style>
:root{
  --blue:#1f5f93;
  --blue-deep:#184f7c;
  --blue-footer:#133f66;
  --blue-title:#2a86c2;
  --red:#a3161d;
  --red-dark:#7e0f14;
  --red-text:#b0141c;
  --sky:#dfe8ef;
  --paper:#f2f4f6;
  --ink:#4a5560;
  --white:#ffffff;
}
*{margin:0;padding:0;box-sizing:border-box}
html,body{width:1200px;height:1027px;overflow:hidden}
body{
  position:relative;
  font-family:"PT Sans",Arial,sans-serif;
  background:linear-gradient(180deg,#edf2f6 0,#d6e2eb 480px,var(--blue) 580px,var(--blue-deep) 940px);
  color:var(--white);
}
.main-nav{position:absolute;left:0;top:0;width:1200px;height:62px}
.main-nav ul{list-style:none;display:flex;position:absolute;left:106px;top:18px;gap:0}
.main-nav li{font-family:"Cuprum",sans-serif;font-size:19px;color:#555e66;margin-right:34px;padding-bottom:4px}
.main-nav li.active{color:var(--blue-title);border-bottom:2px solid var(--blue-title)}
.hero{position:absolute;left:97px;top:84px;width:1005px;height:334px;background:linear-gradient(180deg,#f7f8f9,#e6ebee);border:1px solid #d0d7dc;overflow:hidden}
.hero-art{position:absolute;right:0;top:0;width:500px;height:334px;background:linear-gradient(90deg,rgba(230,234,237,0) 0,#dde1e4 30%,#cfd4d8 100%)}
.hero-title{position:absolute;left:109px;top:190px;font-size:34px;color:var(--blue-title);font-weight:400}
.hero-text{position:absolute;left:109px;top:234px;width:420px;font-size:14px;line-height:17px;color:var(--red-text);font-weight:700}
.hero-arrow{position:absolute;top:130px}
.features{position:absolute;left:97px;top:437px;width:1005px;height:203px;background:var(--red);display:flex}
.feature{position:relative;width:251px;height:203px}
.feature-icon{position:absolute;left:16px;top:22px;width:60px;height:66px}
.feature h2{position:absolute;left:106px;top:20px;font-size:21px;line-height:22px;font-weight:400;text-transform:uppercase}
.feature p{position:absolute;left:16px;top:70px;width:218px;font-size:11px;line-height:13px;padding-left:90px}
.feature .btn{position:absolute;right:14px;bottom:18px;width:100px;height:30px;background:var(--red-dark);font-size:14px;line-height:30px;text-align:center;text-transform:uppercase}
.content{position:absolute;left:97px;top:664px;width:1005px}
.content h1{font-size:24px;font-weight:700;padding-bottom:10px;border-bottom:1px solid rgba(255,255,255,.45)}
.content p{font-size:11.5px;line-height:15px;margin-top:18px;color:#e8eef4}
.site-footer{position:absolute;left:0;top:941px;width:1200px;height:86px;background:var(--blue-footer)}
.footer-nav{position:absolute;left:97px;top:14px;font-size:13px;display:flex;gap:12px}
.copyright{position:absolute;left:97px;top:40px;font-size:13px}
</style>
</head>
<body>
<nav class="main-nav">
  <ul>
    <li>Biografia</li><li>Libri</li><li class="active">Pubblicazioni scientifiche</li><li>Conferenze</li><li>Attività didattica</li><li>Attività medica</li><li>News</li><li>Link</li><li>Contatti</li>
  </ul>
</nav>

<section class="hero">
  <div class="hero-art" role="img" aria-label="Pen sketch of an anatomical study drawn on paper"></div>
  <svg class="hero-arrow" style="left:8px" width="40" height="70" viewBox="0 0 40 70"><polyline points="34,4 6,35 34,66" fill="none" stroke="#b9c0c6" stroke-width="6"/></svg>
  <svg class="hero-arrow" style="right:8px" width="40" height="70" viewBox="0 0 40 70"><polyline points="6,4 34,35 6,66" fill="none" stroke="#b9c0c6" stroke-width="6"/></svg>
  <h1 class="hero-title">Prof. Benedetto L. Caramuzza</h1>
  <p class="hero-text">Vivamus consectetur sem at dolor imperdiet non mollis magna ullamcorper. Praesent tempus, nunc sed ullamcorper gravida, orci justo rhoncus nisi, at adipiscing metus dolor eget nunc.</p>
</section>

<section class="features">
  <article class="feature">
    <div class="feature-icon" role="img" aria-label="Portrait icon of the professor" style="background:linear-gradient(180deg,#c9ccd0,#5b6068)"></div>
    <h2>About<br>the profesor</h2>
    <p>Cum sociis natoque penatibus et magnis dis parturient montes. Curabitur accumsan pellentesque arcu, non cursus erat vehicula sit.</p>
    <div class="btn">Read more</div>
  </article>
  <article class="feature">
    <svg class="feature-icon" viewBox="0 0 60 66"><rect x="14" y="2" width="40" height="54" fill="#cfd3d6"/><rect x="9" y="6" width="40" height="54" fill="#e3e6e8"/><rect x="4" y="10" width="40" height="54" fill="#fff"/><g stroke="#b9bec2" stroke-width="2"><line x1="10" y1="22" x2="38" y2="22"/><line x1="10" y1="30" x2="38" y2="30"/><line x1="10" y1="38" x2="38" y2="38"/><line x1="10" y1="46" x2="30" y2="46"/></g></svg>
    <h2>Libri</h2>
    <p>Nulla et odio pellentesque dolor laor vel commodo. Pellentesque et rutrum tellus. Sed eget ipsum euismod.</p>
    <div class="btn">Read more</div>
  </article>
  <article class="feature">
    <svg class="feature-icon" viewBox="0 0 60 66"><path d="M4 18h38a4 4 0 0 1 4 4v18a4 4 0 0 1-4 4H18l-10 9v-9H4a4 4 0 0 1-4-4V22a4 4 0 0 1 4-4z" fill="#c3c9ce"/><path d="M22 8h34a4 4 0 0 1 4 4v16a4 4 0 0 1-4 4h-2v8l-8-8H22a4 4 0 0 1-4-4V12a4 4 0 0 1 4-4z" fill="#8ea0ad"/></svg>
    <h2>Conferenze</h2>
    <p>Mauris quis felis in nulla laoreet malesuada at id leo. Praesent vel nibh tortor, id interdum orci.</p>
    <div class="btn">Book now</div>
  </article>
  <article class="feature">
    <svg class="feature-icon" viewBox="0 0 60 66"><path d="M8 2h32l14 14v48H8z" fill="#fff"/><path d="M40 2v14h14z" fill="#cfd3d6"/><g stroke="#b9bec2" stroke-width="2"><line x1="15" y1="26" x2="47" y2="26"/><line x1="15" y1="34" x2="47" y2="34"/><line x1="15" y1="42" x2="47" y2="42"/><line x1="15" y1="50" x2="36" y2="50"/></g></svg>
    <h2>Pubblicazioni<br>scientifiche</h2>
    <p>Phasellus faucibus mi a ipsum egestas viverra. Suspendisse in elementum nunc, sed metus blandit posuere.</p>
    <div class="btn">Read more</div>
  </article>
</section>

<main class="content">
  <h1>Lorem ipsum dolor sit amet, consectetur adipiscing elit.</h1>
  <p>Integer id scelerisque turpis. In vestibulum purus a orci placerat facilisis aliquet mauris sollicitudin. Aliquam erat volutpat. Morbi eget gravida dui. Suspendisse in elementum nunc. Cras consequat erat id luctus ornare sit amet tristique tellus varius. Maecenas ullamcorper varius turpis eu dignissim. Pellentesque condimentum venenatis imperdiet. Pellentesque dignissim sem pulvinar leo faucibus rutrum. In congue rhoncus magna, ut vulputate ipsum vestibulum a. Suspendisse eu orci urna, id hendrerit ipsum. Curabitur tincidunt aliquam nulla a tristique. Fusce imperdiet placerat viverra.</p>
  <p>Praesent interdum vehicula auctor. Donec lacus ipsum, elementum vel condimentum fringilla, ultrices in turpis. Praesent erat nunc, pellentesque in sollicitudin et, eleifend et magna. Etiam ultrices pharetra metus vitae fermentum. Pellentesque pretium ullamcorper nisl sit amet posuere. Curabitur nec nibh ut massa sodales aliquet. Quisque ac odio et leo tempor mollis sit amet, ut ornare. Pellentesque rhoncus nibh vel viverra lacinia porttitor. Cras rutrum lacinia odio nec varius. Etiam accumsan enim quis mauris dictum adipiscing. Aliquam mollis mattis enim, a tempor libero mattis nec. Vivamus et vehicula sem. In egestas ultrices scelerisque. Morbi mollis venenatis luctus. Sed eget augue sapien, placerat et varius in, ultrices in metus. Vivamus eu metus eu ipsum dignissim consequat eget non lacus. Etiam aliquam nisi sit tortor fringilla at eleifend sapien malesuada. Morbi ac lacus rhoncus metus sollicitudin pretium sit amet arcu. Suspendisse at arcu at leo luctus semper.</p>
</main>

<footer class="site-footer">
  <div class="footer-nav"><span>Biografia</span><span>|</span><span>Libri</span><span>|</span><span>Pubblicazioni scientifiche</span><span>|</span><span>Conferenze</span><span>|</span><span>Attività didattica</span><span>|</span><span>Attività medica</span><span>|</span><span>News</span><span>|</span><span>Link</span><span>|</span><span>Contatti</span></div>
  <div class="copyright">Prof. Benedetto L. Caramuzza © All Rights Reserved 2012</div>
</footer>
</body>
</html>
```